New retail box design

We are looking at changing our packaging for retilers. I have templates of boxes and like a great design for new packaging.

I will attach pictures of our current packaging.

Industry/Entity Type

Ammunition manufacturing

Requirements
Must have
• warning label and company name

```html
<!DOCTYPE html>
<html lang="en">
<head>
<meta charset="utf-8">
<title>Liberty Forge Ammo LLC – Retail Box Panels</title>
<link rel="stylesheet" href="https://fonts.googleapis.com/css2?family=Oswald:wght@600&family=Crimson+Text:wght@400&display=swap">
<style>
  :root {
    --page-bg: #e6e6e6;
    --brand-red: #9c0b0e;
    --brand-red-dark: #760709;
    --navy: #00263b;
    --navy-dark: #001f31;
    --label-grey: #a4a2a3;
    --type-grey: #b4b2b3;
    --sticker-type: #c9c7c8;
    --rule-red: #a30f12;
  }
  * { box-sizing: border-box; margin: 0; padding: 0; }
  html, body { width: 1200px; height: 1200px; overflow: hidden; }
  body {
    background: var(--page-bg);
    display: flex;
    align-items: center;
    justify-content: center;
  }
  .box-dieline {
    display: flex;
    height: 760px;
    box-shadow: 0 20px 40px rgba(0,0,0,0.12);
  }
  .panel { position: relative; height: 100%; display: flex; flex-direction: column; }
  .panel--side { width: 360px; }
  .panel--front { width: 640px; }

  .band-red { height: 210px; }
  .panel--side .band-red { background: var(--brand-red-dark); padding: 40px 26px 0; }
  .panel--front .band-red {
    background: var(--brand-red);
    display: flex; align-items: center; justify-content: center;
    padding: 0 40px;
  }
  .field-navy { flex: 1; position: relative; }
  .panel--side .field-navy { background: var(--navy-dark); padding: 30px 26px; }
  .panel--front .field-navy { background: var(--navy); }

  .warning-text {
    font-family: "Crimson Text", serif;
    color: var(--type-grey);
    font-size: 27px;
    line-height: 1.15;
  }
  .safety-title {
    font-family: "Crimson Text", serif;
    color: var(--rule-red);
    font-size: 17px;
    margin-bottom: 8px;
  }
  .safety-list {
    list-style: none;
    font-family: "Crimson Text", serif;
    color: var(--type-grey);
    font-size: 18.5px;
    line-height: 1.3;
  }
  .safety-list li { padding-left: 10px; text-indent: -10px; }
  .safety-list li::before { content: "• "; }

  .brand-name {
    font-family: "Crimson Text", serif;
    font-weight: 400;
    color: var(--type-grey);
    font-size: 60px;
    line-height: 1.05;
    text-align: center;
  }
  .sticker-area {
    position: absolute;
    left: 70px; top: 60px;
    width: 500px; height: 380px;
    background: var(--label-grey);
    border-radius: 36px;
    display: flex; align-items: center; justify-content: center;
  }
  .sticker-label {
    font-family: "Oswald", sans-serif;
    font-weight: 600;
    color: var(--sticker-type);
    font-size: 54px;
    text-transform: uppercase;
  }
</style>
</head>
<body>
  <main class="box-dieline">
    <section class="panel panel--side">
      <div class="band-red">
        <p class="warning-text">Warning: Keep out of reach of children.</p>
      </div>
      <div class="field-navy" role="img" aria-label="Navy field with faint line pattern of rifles and magazines">
        <h2 class="safety-title">Safety Rules:</h2>
        <ul class="safety-list">
          <li>Watch your muzzle. Keep gun pointed in safe direction.</li>
          <li>Wear eye and ear protection.</li>
          <li>If gun fails to fire, keep it pointed in a safe direction, then unload carefully avoiding exposure to breech.</li>
          <li>Know your target and what is beyond it.</li>
          <li>Treat every gun as if it were loaded. Don't rely on the safety.</li>
          <li>Keep barrel clear of obstructions.</li>
          <li>Never load a gun until ready to use.</li>
          <li>Only use ammunition that exactly matches markings on your gun.</li>
        </ul>
      </div>
    </section>
    <section class="panel panel--front">
      <header class="band-red">
        <h1 class="brand-name">Liberty Forge<br>Ammo LLC</h1>
      </header>
      <div class="field-navy" role="img" aria-label="Navy field with faint line pattern of rifles and magazines">
        <div class="sticker-area">
          <span class="sticker-label">Sticker Area</span>
        </div>
      </div>
    </section>
  </main>
</body>
</html>
```